Hispanic Financial Counseling and Advocate Firm seeks business card design

Looking for a clean, professional business card design. This is a firm that specializes in providing financial education, coaching, and planning to the Hispanic community. The name of the company is Valemar, which means to prosper. We need a design that is clean, professional, and invokes trust, professionalism, but also welcoming. Our logo is a plant growing from a hand to give the messaging of of being in control of growing your financial future and security. Its part of a larger organization names Celesta Financial Group, who's logo is a tree with multi colored branches. We have the back of the card designed so we just need the front designed. the back is blue, so front needs to be a different background color, not blue.

Target Market(s)

Hispanic Community looking to better their future

Industry/Entity Type

financial services

Contact Information for Business Card

contact info: Anselmo Ibarra Jr, 951-555-0147, info@celestafinancialgroup.example. Celestafinancialgroup.example. tag line: Para un futuro mas seguro!

Requirements
Must have
• basics: logo, contact info.
Nice to have
• possibly incorporate the tree logo provided somehow
Should not have
• should not look like the back, needs to be different from the back provided.

```html
<!DOCTYPE html>
<html lang="es">
<head>
<meta charset="utf-8">
<title>Valemar – Business Card Front</title>
<link rel="stylesheet" href="https://fonts.googleapis.com/css2?family=Jost:ital,wght@0,400;0,500;0,600;0,800;1,400&display=swap">
<style>
  :root {
    --leaf-green: #6aa42f;
    --slate: #4a5872;
    --pale-leaf: #d4e4c1;
    --paper: #ffffff;
    --stage: #ffffff;
  }
  * { margin: 0; padding: 0; box-sizing: border-box; }
  html, body {
    width: 1200px; height: 793px; overflow: hidden;
    background: var(--stage);
    font-family: "Jost", "Futura", sans-serif;
  }
  .card {
    position: absolute; left: 66px; top: 66px;
    width: 1069px; height: 662px;
    border-radius: 48px; overflow: hidden;
    background: var(--paper);
    box-shadow: 0 4px 28px rgba(0,0,0,0.28);
  }
  .foliage {
    position: absolute; left: 521px; top: 0;
    width: 548px; height: 400px;
    background: radial-gradient(ellipse at 65% 45%, var(--pale-leaf) 0%, rgba(212,228,193,0.55) 55%, rgba(255,255,255,0) 80%);
  }
  .brand {
    position: absolute; left: 116px; top: 118px;
  }
  .brand-mark {
    display: block; width: 90px; height: 90px; border-radius: 50%;
    background: var(--leaf-green);
    margin: 0 0 32px 100px;
  }
  .brand-name {
    display: block;
    font-size: 78px; font-weight: 500; line-height: 1;
    color: var(--leaf-green); letter-spacing: 1px;
  }
  .brand-sub {
    display: block; margin-top: 12px;
    font-size: 19px; font-weight: 600; letter-spacing: 3.4px;
    color: var(--slate);
  }
  .contact-band {
    position: absolute; left: 0; top: 400px;
    width: 100%; height: 197px;
    background: var(--slate);
  }
  .person-name {
    position: absolute; left: 73px; top: 72px;
    font-size: 45px; font-weight: 800; line-height: 1.2;
    color: var(--leaf-green);
  }
  .contact-list { list-style: none; position: absolute; left: 577px; top: 0; }
  .contact-item {
    position: absolute; left: 0; white-space: nowrap;
    display: flex; align-items: center; gap: 14px;
    font-size: 27px; font-weight: 400; color: var(--paper);
    height: 40px;
  }
  .contact-item svg { width: 27px; height: 32px; fill: var(--leaf-green); flex: none; }
  .contact-phone { top: 17px; }
  .contact-email { top: 77px; }
  .contact-web { top: 135px; }
  .tagline-band {
    position: absolute; left: 0; top: 597px;
    width: 100%; height: 65px;
    background: var(--leaf-green);
    display: flex; align-items: center; justify-content: center;
  }
  .tagline {
    font-size: 40px; font-style: italic; font-weight: 400;
    color: var(--paper); letter-spacing: 0.5px;
  }
</style>
</head>
<body>
  <div class="card">
    <div class="foliage" role="img" aria-label="Decorative pale green leafy branches"></div>

    <div class="brand">
      <span class="brand-mark"></span>
      <span class="brand-name">Valemar</span>
      <span class="brand-sub">SERVICIOS FINANCIEROS</span>
    </div>

    <div class="contact-band">
      <div class="person-name">Anselmo Ibarra Jr</div>
      <ul class="contact-list">
        <li class="contact-item contact-phone">
          <svg viewBox="0 0 22 32" aria-hidden="true"><rect x="0" y="0" width="22" height="32" rx="3"/><rect x="2" y="4" width="18" height="22" fill="#4a5872"/><circle cx="11" cy="29" r="1.2" fill="#4a5872"/></svg>
          951-555-0147
        </li>
        <li class="contact-item contact-email">
          <svg viewBox="0 0 28 22" aria-hidden="true"><rect x="0" y="0" width="28" height="22" rx="2"/><path d="M3 3 L14 14 L25 3" fill="none" stroke="#4a5872" stroke-width="2.4"/></svg>
          info@celestafinancialgroup.example
        </li>
        <li class="contact-item contact-web">
          <svg viewBox="0 0 28 28" aria-hidden="true"><circle cx="14" cy="14" r="13"/><g fill="none" stroke="#4a5872" stroke-width="1.8"><ellipse cx="14" cy="14" rx="5.5" ry="13"/><line x1="14" y1="1" x2="14" y2="27"/><line x1="1" y1="10" x2="27" y2="10"/><line x1="1" y1="18" x2="27" y2="18"/></g></svg>
          Celestafinancialgroup.example
        </li>
      </ul>
    </div>

    <div class="tagline-band">
      <p class="tagline">Para un futuro mas seguro!</p>
    </div>
  </div>
</body>
</html>
```